Business Card Design for Kidvale (Hires out childrens play areas)

Looking to have a business card designed for a company we just bought. The company rents out childrens play areas.

I have uploaded a couple of examples of the kind of business card style I like. Here are two more examples:

https://quorvastudio.nz/project/bright-romp-branding/
https://imgvaultcdn.com/design_img/8841052/302917/302917_5518203_8841052_b73e19a2_image.jpg

I think a white card will be best due to all the colours in the logo.

Size we require: 3.75" x 2.25" (horizontally orientated) with a 0.125" bleed

Uploaded is two versions of our logo.

Details for the card:
1. My name: Liam Verster
2. Title: Managing Director
3. Phone no: 021 563 417
4. Email: liam@kidvale.co.nz
5. URL: www.kidvale.co.nz
6. Address:
PO Box 318625
Fernlea, Auckland

Let me know if you need anything else.

Target Market(s)

Hospitals, doctors surgeries, bed shops, etc.

Contact Information for Business Card

Details for the card:
1. My name: Liam Verster
3. Phone no: 021 563 417
5. URL: www.kidvale.co.nz
6. Address:
PO Box 318625
Fernlea, Auckland

Requirements
Should not have
• Not too busy.

```html
<!DOCTYPE html>
<html lang="en">
<head>
<meta charset="utf-8">
<title>Kidvale Business Card</title>
<link rel="stylesheet" href="https://fonts.googleapis.com/css2?family=Nunito:wght@800&family=Lato:wght@400&display=swap">
<style>
  :root {
    --page: #e9e7e4;
    --card: #ffffff;
    --panel: #f6f6f7;
    --blue: #1f4fa3;
    --grey: #4a4a4a;
    --muted: #6b6b6b;
    --orange: #f0901e;
    --teal: #1a9a9a;
    --red: #d92a2a;
    --green: #3aaa3f;
    --purple: #8a2c9a;
  }
  * { box-sizing: border-box; margin: 0; padding: 0; }
  html, body { width: 1200px; height: 1200px; overflow: hidden; }
  body {
    background: var(--page);
    font-family: "Lato", Arial, sans-serif;
    position: relative;
  }
  .card {
    position: absolute;
    left: 150px;
    width: 900px;
    height: 514px;
    background: var(--card);
    overflow: hidden;
    box-shadow: 0 10px 30px rgba(0,0,0,0.12);
  }
  .card-front { top: 60px; }
  .card-back { top: 626px; }

  .hex-texture {
    position: absolute;
    top: 0; right: 0;
    width: 60%;
    height: 55%;
    background: radial-gradient(ellipse at 70% 20%, #eeeeef 0%, rgba(255,255,255,0) 70%);
  }
  .brand-name {
    font-family: "Nunito", Arial, sans-serif;
    font-weight: 800;
    color: var(--blue);
    display: flex;
    align-items: center;
    gap: 18px;
    position: absolute;
  }
  .brand-mark {
    border-radius: 50%;
    background: var(--purple);
    flex: none;
  }
  .card-front .brand-name {
    font-size: 96px;
    left: 50%;
    top: 50%;
    transform: translate(-50%, -50%);
  }
  .card-front .brand-mark { width: 60px; height: 60px; }

  .colour-band {
    position: absolute;
    left: 0; right: 0; bottom: 0;
    height: 10px;
    display: flex;
  }
  .colour-band span { flex: 1; }
  .band-teal { background: var(--teal); }
  .band-red { background: var(--red); }
  .band-green { background: var(--green); }
  .band-orange { background: var(--orange); }

  .card-back .brand-name {
    font-size: 64px;
    left: 70px;
    top: 50%;
    transform: translateY(-50%);
    gap: 14px;
  }
  .card-back .brand-mark { width: 40px; height: 40px; }

  .details-panel {
    position: absolute;
    top: 0; right: 0; bottom: 0;
    width: 47%;
    background: var(--panel);
    box-shadow: -8px 0 18px rgba(0,0,0,0.05);
    padding: 110px 0 0 56px;
  }
  .corner-art {
    position: absolute;
    top: -60px; right: -50px;
    width: 170px; height: 170px;
    border-radius: 50%;
    background: radial-gradient(circle at 40% 60%, #f3d9c9 0%, #c97ad0 55%, var(--purple) 100%);
  }
  .person-name {
    font-family: "Nunito", Arial, sans-serif;
    font-weight: 800;
    font-size: 44px;
    color: var(--blue);
    line-height: 1.05;
  }
  .person-title {
    font-size: 20px;
    color: var(--muted);
    margin-top: 4px;
  }
  .address {
    font-size: 24px;
    color: var(--grey);
    line-height: 1.3;
    margin-top: 30px;
  }
  .contact-list {
    list-style: none;
    margin-top: 28px;
    margin-left: 60px;
  }
  .contact-list li {
    display: flex;
    align-items: center;
    gap: 12px;
    font-size: 22px;
    color: var(--grey);
    line-height: 1.55;
  }
  .contact-list svg { width: 20px; height: 20px; flex: none; }
</style>
</head>
<body>

<section class="card card-front">
  <div class="hex-texture" role="img" aria-label="Faint hexagon background pattern"></div>
  <div class="brand-name"><span class="brand-mark"></span>Kidvale</div>
  <div class="colour-band">
    <span class="band-teal"></span>
    <span class="band-red"></span>
    <span class="band-green"></span>
    <span class="band-orange"></span>
  </div>
</section>

<section class="card card-back">
  <div class="brand-name"><span class="brand-mark"></span>Kidvale</div>
  <div class="details-panel">
    <div class="corner-art" role="img" aria-label="Corner crop of the brand character illustration"></div>
    <h1 class="person-name">Liam Verster</h1>
    <p class="person-title">Managing Director</p>
    <p class="address">PO Box 318625<br>Fernlea, Auckland</p>
    <ul class="contact-list">
      <li>
        <svg viewBox="0 0 24 24" aria-hidden="true"><path fill="var(--orange)" d="M6.6 10.8a15 15 0 0 0 6.6 6.6l2.2-2.2a1 1 0 0 1 1-.25 11.4 11.4 0 0 0 3.6.57 1 1 0 0 1 1 1V20a1 1 0 0 1-1 1A17 17 0 0 1 3 4a1 1 0 0 1 1-1h3.5a1 1 0 0 1 1 1c0 1.25.2 2.45.57 3.57a1 1 0 0 1-.25 1z"/></svg>
        021 563 417
      </li>
      <li>
        <svg viewBox="0 0 24 24" aria-hidden="true"><rect x="2" y="5" width="20" height="14" rx="1.5" fill="var(--orange)"/><path d="M3 6l9 7 9-7" fill="none" stroke="#fff" stroke-width="1.6"/></svg>
        liam@kidvale.co.nz
      </li>
      <li>
        <svg viewBox="0 0 24 24" aria-hidden="true" fill="none" stroke="var(--orange)" stroke-width="1.8"><circle cx="12" cy="12" r="9"/><ellipse cx="12" cy="12" rx="4" ry="9"/><path d="M3 12h18M5 7h14M5 17h14"/></svg>
        www.kidvale.co.nz
      </li>
    </ul>
  </div>
</section>

</body>
</html>
```